Flyer for Programming Classes for Kids

We are small school in Tokyo, Japan teaching computer programming to kids in English.
We need a flyer to promote our classes and provide basic information about our company.
See Flyer_Notes.doc for more company info, class info, and flyer requirements.
Basic Info:
One page flyer. Two-sided, front and back.
We would like a flyer that introduces the company. -and-
Highlights the classes we offer
Target Market: 6-12 year old kids and their parents. Audience is English speaking families in Japan.
Look And Feel: Bold, Playful, Modern, Conservative
Paper Size: B4
What is B4? https://www.quorvanta.com/products/resources/paper-sizes-and-formats-explained.php
Target Market(s)
Tokyo, but English speakers
Industry/Entity Type
Education
Colors
Designer to choose colors to be used in the design.
Look and feel
Each slider illustrates characteristics of the customer's brand and the style your logo design should communicate.

```html
<!DOCTYPE html>
<html lang="en">
<head>
<meta charset="utf-8">
<title>Bytewise Lab – Classes Info</title>
<link href="https://fonts.googleapis.com/css2?family=Inter:wght@400;700&display=swap" rel="stylesheet">
<style>
  :root {
    --page-bg: #6e6e6e;
    --paper: #ffffff;
    --ink: #1c1c1c;
    --header-top: #8fc23f;
    --header-top-deep: #3f7a3a;
    --header-band: #3b5a33;
    --header-band-deep: #2f4a2b;
    --brand-lime: #b5e04a;
    --column-tint: #c4df9c;
    --photo-grey: #7d7a74;
    --photo-light: #cfcac0;
    --photo-dark: #3c3a36;
  }
  * { box-sizing: border-box; margin: 0; padding: 0; }
  html, body { width: 1200px; height: 1200px; overflow: hidden; }
  body {
    background: var(--page-bg);
    font-family: "Inter", Arial, sans-serif;
    color: var(--ink);
    position: relative;
  }
  .flyer {
    position: absolute;
    left: 197px; top: 30px;
    width: 806px; height: 1140px;
    background: var(--paper);
    overflow: hidden;
  }
  .flyer-header-strip {
    position: absolute; left: 0; top: 0; width: 100%; height: 60px;
    background: linear-gradient(90deg, var(--header-top-deep), var(--header-top) 40%, #c9d84a 55%, var(--header-top) 75%, var(--header-top-deep));
  }
  .flyer-header {
    position: absolute; left: 0; top: 60px; width: 100%; height: 73px;
    background: linear-gradient(180deg, var(--header-band-deep), var(--header-band));
    display: flex; align-items: center; justify-content: center; gap: 20px;
  }
  .brand-name, .header-title {
    color: var(--brand-lime);
    font-weight: 700;
    font-size: 34px;
    letter-spacing: 0.5px;
  }
  .header-title { font-weight: 400; }
  .class-column {
    position: absolute; left: 0; top: 133px; width: 447px; height: 674px;
    background: linear-gradient(180deg, var(--column-tint) 0%, #eef6e2 45%, var(--paper) 70%);
    padding: 22px 26px 0 29px;
  }
  .class-item { margin-bottom: 14px; }
  .class-title {
    display: flex; align-items: center; gap: 9px;
    font-weight: 700; font-size: 18px; margin-bottom: 6px;
  }
  .class-number {
    width: 21px; height: 21px; border-radius: 50%;
    background: var(--ink); color: var(--paper);
    font-size: 13px; display: flex; align-items: center; justify-content: center;
  }
  .class-points { list-style: none; padding-left: 39px; }
  .class-points li {
    position: relative; font-size: 15px; line-height: 17px; margin-bottom: 7px;
  }
  .class-points li::before {
    content: ""; position: absolute; left: -14px; top: 6px;
    width: 6px; height: 6px; border-radius: 50%; background: var(--ink);
  }
  .photo { position: absolute; }
  .photo-student-laptop {
    left: 447px; top: 133px; width: 359px; height: 350px;
    background: linear-gradient(160deg, var(--photo-light), var(--photo-grey) 60%, var(--photo-dark));
  }
  .photo-classroom {
    left: 447px; top: 483px; width: 359px; height: 324px;
    background: linear-gradient(200deg, #d8d6d2, #8e8a84 55%, #5b5752);
  }
  .photo-robot-build {
    left: 0; top: 807px; width: 447px; height: 333px;
    background: linear-gradient(180deg, #9aa4b4, #3a3a3a 55%, #1f1f1f);
  }
  .curriculum-note {
    position: absolute; left: 487px; top: 870px; width: 290px;
    font-size: 18px; line-height: 23px;
  }
  .curriculum-note p + p { margin-top: 9px; }
</style>
</head>
<body>
  <main class="flyer">
    <div class="flyer-header-strip"></div>
    <header class="flyer-header">
      <span class="brand-name">Bytewise Lab</span>
      <span class="header-title">Classes Info</span>
    </header>

    <section class="class-column">
      <article class="class-item">
        <h2 class="class-title"><span class="class-number">1</span>Beginner TileCode</h2>
        <ul class="class-points">
          <li>For kids new to coding. Learn to program using TileCode, a fun and easy to use language. Make games, interactive stories, animations, and more, all while learning the fundamentals of computer programming.</li>
          <li>For students with little or no experience.</li>
        </ul>
      </article>
      <article class="class-item">
        <h2 class="class-title"><span class="class-number">2</span>Intermediate TileCode</h2>
        <ul class="class-points">
          <li>Kids learn more advanced programming concepts in TileCode and create larger and more complex programs. They plan, design, and create their own coding projects, from start to finish.</li>
          <li>For students who have completed Beginner TileCode 1 &amp; 2 or have prior coding experience.</li>
        </ul>
      </article>
      <article class="class-item">
        <h2 class="class-title"><span class="class-number">3</span>Tinker Garage Workshop</h2>
        <ul class="class-points">
          <li>Continue to learn and explore coding in a collaborative, fun space. Each lesson kids complete a new, STEM based coding project. Projects cover Physics, Math, Story Telling, Game Design, BrickBot Robotics, and more.</li>
          <li>Recommended for intermediate students.</li>
        </ul>
      </article>
      <article class="class-item">
        <h2 class="class-title"><span class="class-number">4</span>Viperscript</h2>
        <ul class="class-points">
          <li>Learn to code in one of the most popular text based languages. Viperscript 101 teaches kids the basics of Viperscript coding with an emphasis on Mathematics and computer science fundamentals.</li>
          <li>For students aged 12-17 with little or no experience.</li>
        </ul>
      </article>
    </section>

    <div class="photo photo-student-laptop" role="img" aria-label="Photo of a child working on a block coding program on a laptop"></div>
    <div class="photo photo-classroom" role="img" aria-label="Photo of a classroom with kids coding at laptops and a teacher helping"></div>
    <div class="photo photo-robot-build" role="img" aria-label="Photo of a small brick-built robot in front of a laptop showing block code"></div>

    <section class="curriculum-note">
      <p>Our curriculum is based on STEM (Science, Technology, Engineering, and Math) with a pinch of Art, and whole lot of creativity.</p>
      <p>Kids learn core, computer science fundamentals while solving STEM based projects and tapping into their creative minds.</p>
    </section>
  </main>
</body>
</html>
```